BRICKWORK BLUEPRINT: THE RELIABLE WAY TO EARN HUGE GAINS FROM BUDGET HOME UPGRADES

I am looking for a book cover design for my new E-Book.

My idea for the design is a pin board with before and after photos of our properties pinned on it (example attached). I have also attached some photos to use.

PLEASE SUBMIT OTHER DESIGNS ALSO AS THIS WAS JUST AN IDEA BUT I AM OPEN TO OTHER IDEAS ALSO.

Page size is 5x7 inches

Font styles to use
Serif
Sans Serif

Colors
0255a3
3176b5
85acd3
85cae6
33a6d7
0392cd
9bcb3c
abd036
ec1f27

```html
<!DOCTYPE html>
<html lang="en">
<head>
<meta charset="utf-8">
<title>Brickwork Blueprint – Book Cover</title>
<link rel="stylesheet" href="https://fonts.googleapis.com/css2?family=Oswald:wght@700&family=Roboto:wght@900&display=swap">
<style>
  :root {
    --navy: #0255a3;
    --sky: #85cae6;
    --sky-glow: #c9ecf8;
    --red: #ec1f27;
    --white: #ffffff;
    --stage: #ffffff;
  }
  * { margin: 0; padding: 0; box-sizing: border-box; }
  html, body { width: 1200px; height: 1000px; overflow: hidden; background: var(--stage); }
  .canvas { position: relative; width: 1200px; height: 1000px; }

  .cover {
    position: absolute; left: 271px; top: 40px;
    width: 658px; height: 920px;
    background:
      radial-gradient(ellipse 300px 90px at 50% 770px, var(--sky-glow) 0%, rgba(201,236,248,0) 100%),
      var(--sky);
    overflow: hidden;
  }

  .title {
    position: absolute; left: 0; width: 100%; text-align: center;
    font-family: "Oswald", "Arial Narrow", sans-serif; font-weight: 700;
    line-height: 1; letter-spacing: 1px;
  }
  .title-top { top: 2px; font-size: 84px; color: var(--navy); }
  .title-main { top: 90px; font-size: 104px; color: var(--white); }

  .photo {
    position: absolute;
  }
  .col-left { left: 38px; width: 273px; }
  .col-right { left: 322px; width: 299px; }
  .row-1 { top: 205px; height: 157px; }
  .row-2 { top: 375px; height: 155px; }
  .row-3 { top: 545px; height: 157px; }

  .photo-before-1 { background: linear-gradient(180deg, #b9c6cf 0%, #e4e2da 45%, #8d8a7f 100%); }
  .photo-after-1  { background: linear-gradient(180deg, #c8d4de 0%, #4a5577 45%, #2f3547 80%, #7a8a6a 100%); }
  .photo-before-2 { background: linear-gradient(180deg, #d8dfe4 0%, #a8a89b 45%, #7c7466 100%); }
  .photo-after-2  { background: linear-gradient(180deg, #6d8aa8 0%, #c8c8c0 45%, #5f7a3c 100%); }
  .photo-before-3 { background: linear-gradient(180deg, #d9e3ea 0%, #e8e4dc 40%, #6f7a55 100%); }
  .photo-after-3  { background: linear-gradient(180deg, #8fbde6 0%, #d4d6d8 45%, #63a43e 100%); }

  .tag {
    position: absolute; width: 130px; height: 27px;
    border-radius: 50%;
    background: var(--red); color: var(--white);
    font-family: "Roboto", Arial, sans-serif; font-weight: 900;
    font-size: 19px; letter-spacing: 0.5px;
    display: flex; align-items: center; justify-content: center;
  }
  .tag-before { left: 23px; }
  .tag-after { left: 505px; }
  .tag-row-1 { top: 350px; }
  .tag-row-2 { top: 525px; }

  .subtitle {
    position: absolute; left: 0; top: 728px; width: 100%;
    text-align: center;
    font-family: "Roboto", Arial, sans-serif; font-weight: 900;
    font-size: 25px; line-height: 31px; letter-spacing: 0.5px;
    color: var(--white);
  }
  .subtitle-accent { color: var(--red); }

  .author-band {
    position: absolute; left: 0; top: 832px; width: 100%; height: 88px;
    background: var(--navy);
    color: var(--white); text-align: center;
    font-family: "Roboto", Arial, sans-serif; font-weight: 900;
    font-size: 20px; line-height: 30px; letter-spacing: 0.5px;
    padding-top: 13px;
  }
</style>
</head>
<body>
<div class="canvas">
  <div class="cover">
    <h1 class="title title-top">BRICKWORK</h1>
    <div class="title title-main">BLUEPRINT</div>

    <div class="photo col-left row-1 photo-before-1" role="img" aria-label="Photo of a two-storey house before renovation"></div>
    <div class="photo col-right row-1 photo-after-1" role="img" aria-label="Photo of the same two-storey house after renovation, painted dark blue"></div>
    <div class="photo col-left row-2 photo-before-2" role="img" aria-label="Photo of a backyard and carport before renovation"></div>
    <div class="photo col-right row-2 photo-after-2" role="img" aria-label="Photo of the renovated cottage with new deck and lawn"></div>
    <div class="photo col-left row-3 photo-before-3" role="img" aria-label="Photo of a raised timber house with a red roof before renovation"></div>
    <div class="photo col-right row-3 photo-after-3" role="img" aria-label="Photo of the renovated grey house with white verandah"></div>

    <div class="tag tag-before tag-row-1">BEFORE</div>
    <div class="tag tag-after tag-row-1">AFTER</div>
    <div class="tag tag-before tag-row-2">BEFORE</div>
    <div class="tag tag-after tag-row-2">AFTER</div>

    <p class="subtitle">
      THE RELIABLE WAY TO EARN<br>
      HUGE GAINS FROM<br>
      <span class="subtitle-accent">BUDGET HOME UPGRADES!</span>
    </p>

    <div class="author-band">
      CREATED AND WRITTEN BY MARCUS ELLORY<br>
      ELLORY HOMES + BUILD IT BETTER
    </div>
  </div>
</div>
</body>
</html>
```